Bingo Night

Willowmere Terraces is an Assisted Living Facility. We have 34 residents currently living in our facility. We provide care for elderly patients that need a slightly higher level of care than what can be provided at home. We are sending out this invitation to people in the surrounding community for Bingo night March 19, 2014 @ 6:00pm. The colors we would like to use are gold & maroon. Our address is 2947 W 38th St Tulsa, OK 74107. 918-562-3049. Also, the phrase "open to the public" should be incorporated on both sides.
Updates

Target Market(s)

Men and women between the ages of 50-90 years old.

Industry/Entity Type

Community

Font styles to use
Serif
Script

Requirements
Must have
• At least 4 pictures provided, our address, time of event, and phone number.

```html
<!DOCTYPE html>
<html lang="en">
<head>
<meta charset="utf-8">
<title>Bingo Night – Willowmere Terraces</title>
<link rel="stylesheet" href="https://fonts.googleapis.com/css2?family=Poiret+One&family=Zilla+Slab:ital,wght@1,700&display=swap">
<style>
  :root {
    --maroon: #8b1a1e;
    --maroon-deep: #7a1518;
    --gold: #f4c41c;
    --gold-dark: #c8951a;
    --paper: #ffffff;
    --page: #ffffff;
  }
  * { margin: 0; padding: 0; box-sizing: border-box; }
  html, body { width: 1200px; height: 1000px; overflow: hidden; background: var(--page); }
  .flyer {
    position: absolute; left: 200px; top: 180px;
    width: 815px; height: 630px;
    background: var(--paper); overflow: hidden;
  }
  .garden-photo {
    position: absolute; left: 0; top: 455px; width: 470px; height: 175px;
    background: linear-gradient(180deg, #b9c2c6 0%, #cfd3cf 30%, #6f8f4a 55%, #8a8f84 75%, #5e7f3a 100%);
    -webkit-mask-image: linear-gradient(90deg, #000 78%, transparent 100%);
            mask-image: linear-gradient(90deg, #000 78%, transparent 100%);
  }
  .backdrop { position: absolute; left: 0; top: 0; width: 815px; height: 630px; }
  .ornament {
    position: absolute;
    background: radial-gradient(circle, rgba(244,196,28,0.35) 0%, rgba(200,149,26,0.55) 100%);
    border-radius: 4px;
  }
  .frame {
    position: absolute;
    background: linear-gradient(135deg, var(--gold-dark), var(--gold) 50%, var(--gold-dark));
  }
  .photo { position: absolute; }
  .photo--lobby { background: linear-gradient(135deg, #d9a56a, #b07a4a 50%, #8a5a3a); }
  .photo--dining { background: linear-gradient(135deg, #9a8a78, #c9c0b0 50%, #6a6a5a); }
  .photo--chef { background: linear-gradient(180deg, #c9c7c0, #8d7f70 60%, #4a3f38); }
  .event-title {
    position: absolute; left: 72px; top: 232px;
    font-family: "Poiret One", sans-serif; font-size: 100px; font-weight: 400;
    color: var(--gold); letter-spacing: 2px; line-height: 1; white-space: nowrap;
  }
  .event-date {
    position: absolute; left: 170px; top: 410px;
    font-family: "Zilla Slab", serif; font-style: italic; font-weight: 700;
    font-size: 27px; color: var(--gold); word-spacing: 3px; white-space: nowrap;
  }
  .contact {
    position: absolute; right: 40px; top: 495px; text-align: right;
    font-family: "Zilla Slab", serif; font-style: italic; font-weight: 700;
    font-size: 22px; line-height: 36px; color: var(--maroon);
  }
</style>
</head>
<body>
<main class="flyer">
  <div class="garden-photo" role="img" aria-label="Photo of the facility courtyard garden with shrubs and a rock waterfall"></div>

  <svg class="backdrop" viewBox="0 0 815 630" aria-hidden="true">
    <defs>
      <linearGradient id="goldBand" x1="0" x2="1" y1="0" y2="0">
        <stop offset="0" stop-color="#c8951a"/>
        <stop offset="0.5" stop-color="#f7d334"/>
        <stop offset="1" stop-color="#c8951a"/>
      </linearGradient>
    </defs>
    <path d="M0 438 Q420 565 815 386 V412 Q420 590 0 462 Z" fill="url(#goldBand)"/>
    <path d="M0 0 H815 V388 Q420 562 0 442 Z" fill="var(--maroon)"/>
  </svg>

  <div class="ornament" style="left:35px;top:35px;width:240px;height:180px" role="img" aria-label="Gold scroll ornament framing a photo"></div>
  <div class="frame" style="left:55px;top:70px;width:200px;height:112px"></div>
  <div class="photo photo--lobby" style="left:65px;top:78px;width:182px;height:96px" role="img" aria-label="Photo of the lobby with a flower arrangement"></div>

  <div class="ornament" style="left:318px;top:35px;width:240px;height:180px" role="img" aria-label="Gold scroll ornament framing a photo"></div>
  <div class="frame" style="left:338px;top:70px;width:200px;height:112px"></div>
  <div class="photo photo--dining" style="left:348px;top:78px;width:182px;height:96px" role="img" aria-label="Photo of residents seated in the dining room"></div>

  <div class="ornament" style="left:590px;top:35px;width:180px;height:240px" role="img" aria-label="Gold scroll ornament framing a photo"></div>
  <div class="frame" style="left:625px;top:55px;width:107px;height:202px"></div>
  <div class="photo photo--chef" style="left:633px;top:63px;width:92px;height:186px" role="img" aria-label="Photo of a chef statue holding a menu board"></div>

  <h1 class="event-title">Bingo Night</h1>
  <p class="event-date">March 19, 2014 &nbsp;@ 6:00pm</p>

  <address class="contact">
    2947 W 38th St Tulsa<br>
    OK 74107<br>
    918-562-3049
  </address>
</main>
</body>
</html>
```